table invoices in a modern format! (make it fun to look at!!)

Our has invoices that are shown to our clients. This is currently done in a normal table view, but its boring to look at and is not modern.
We would like to have a modern look and feel
it should ABSOLUTLY not be in table form.
Cards, graphs, pictures, whatever... should be fun and almost interactive.

the table file is how it current looks like.
the other two files were "ideas" to have a better representation
IT DOES NOT NEED TO LOOK LIKE THAT if you have a better idea please go for it.

secondary objective, the graphs/cards/whatever you design should be interactive, meaning I can "click on it" to pay a bill, or see more info.

Let me know if there are more questions!

```html
<!DOCTYPE html>
<html lang="en">
<head>
<meta charset="utf-8">
<title>Invoices Overview 2019</title>
<link href="https://fonts.googleapis.com/css2?family=Rubik:wght@400;500;700&display=swap" rel="stylesheet">
<style>
  :root{
    --backdrop:#21124f;
    --backdrop-deep:#170c3a;
    --sheet:#ffffff;
    --tab-dark:#3d3a4b;
    --tab-band:#e1ddf0;
    --tab-active:#3c27a6;
    --ink:#2e2b3a;
    --ink-soft:#555260;
    --plot:#fafafa;
    --grid:#e3e3e3;
    --contract:#4db5ff;
    --extra:#7a4dff;
    --unpaid:#ff5a3c;
    --plus:#ff4ee0;
    --days:#fddf62;
    --paid:#35d99f;
    --tip:#5a5a5a;
    --tip-link:#ffe14d;
  }
  *{box-sizing:border-box;margin:0;padding:0}
  html,body{width:1200px;height:1050px;overflow:hidden}
  body{background:radial-gradient(ellipse at center,var(--backdrop) 40%,var(--backdrop-deep) 100%);font-family:"Rubik",sans-serif;color:var(--ink)}
  .stage{position:absolute;left:0;top:0;width:1600px;height:1400px;transform:scale(.75);transform-origin:0 0}
  .sheet{position:absolute;left:100px;top:100px;width:1400px;height:1200px;background:var(--sheet)}

  .year-tabs{position:absolute;left:215px;top:204px;width:1170px;height:59px;background:var(--tab-band);display:flex;align-items:center}
  .year-tabs__title{width:292px;height:59px;background:var(--tab-dark);color:#fff;font-weight:500;font-size:21px;display:flex;align-items:center;justify-content:flex-end;padding-right:33px}
  .year-tab{font-size:21px;font-weight:500;color:var(--ink);text-decoration:none;position:absolute;top:18px}
  .year-tab--active{top:-9px;height:77px;width:105px;background:var(--tab-active);color:#fff;display:flex;align-items:center;justify-content:center;box-shadow:0 2px 6px rgba(0,0,0,.2)}

  .legend{position:absolute;left:772px;top:340px;display:grid;grid-template-columns:173px 237px auto;row-gap:6px;font-size:14px;color:var(--ink-soft)}
  .legend__item{display:flex;align-items:center;gap:12px;white-space:nowrap}
  .legend__swatch{width:12px;height:12px}

  .chart{position:absolute;left:0;top:0}
  .chart text{font-family:"Rubik",sans-serif}
  .axis-label{font-size:14px;fill:var(--ink-soft)}
  .axis-title{font-size:15px;font-weight:500;fill:var(--ink)}
  .bar-note{font-size:10px;fill:var(--ink-soft)}
  .tip-box{fill:var(--tip)}
  .tip-id{font-size:12px;font-weight:700;fill:#fff}
  .tip-line{font-size:12px;fill:#fff}
  .tip-pay{font-size:11px;font-weight:700;fill:var(--tip-link);text-decoration:underline}
  .invoice-bar{cursor:pointer}
</style>
</head>
<body>
<div class="stage">
  <div class="sheet"></div>

  <nav class="year-tabs">
    <div class="year-tabs__title">Invoices Prior</div>
    <a class="year-tab year-tab--active" style="left:330px" href="#y2019">2019</a>
    <a class="year-tab" style="left:467px" href="#y2020">2020</a>
    <a class="year-tab" style="left:581px" href="#y2021">2021</a>
    <a class="year-tab" style="left:690px" href="#y2022">2022</a>
    <a class="year-tab" style="left:803px" href="#y2023">2023</a>
  </nav>

  <ul class="legend">
    <li class="legend__item"><span class="legend__swatch" style="background:var(--contract)"></span>CONTRACT PRICE</li>
    <li class="legend__item"><span class="legend__swatch" style="background:var(--unpaid)"></span>MINUSE BALANCE / UNPAID</li>
    <li class="legend__item"><span class="legend__swatch" style="background:var(--days)"></span>DAYS</li>
    <li class="legend__item"><span class="legend__swatch" style="background:var(--extra)"></span>EXTRA CREDIT</li>
    <li class="legend__item"><span class="legend__swatch" style="background:var(--plus)"></span>PLUS BALANCE</li>
    <li class="legend__item"><span class="legend__swatch" style="background:var(--paid)"></span>RECEIVED PAYMENT / PAID</li>
  </ul>

  <svg class="chart" width="1600" height="1400" viewBox="0 0 1600 1400">
    <rect x="328" y="452" width="968" height="541" fill="var(--plot)"/>
    <g stroke="var(--grid)" stroke-width="1">
      <line x1="328" x2="1296" y1="482" y2="482"/><line x1="328" x2="1296" y1="512" y2="512"/>
      <line x1="328" x2="1296" y1="542" y2="542"/><line x1="328" x2="1296" y1="572" y2="572"/>
      <line x1="328" x2="1296" y1="602" y2="602"/><line x1="328" x2="1296" y1="632" y2="632"/>
      <line x1="328" x2="1296" y1="662" y2="662"/><line x1="328" x2="1296" y1="692" y2="692"/>
      <line x1="328" x2="1296" y1="722" y2="722"/><line x1="328" x2="1296" y1="752" y2="752"/>
      <line x1="328" x2="1296" y1="782" y2="782"/><line x1="328" x2="1296" y1="812" y2="812"/>
      <line x1="328" x2="1296" y1="842" y2="842"/><line x1="328" x2="1296" y1="872" y2="872"/>
      <line x1="328" x2="1296" y1="902" y2="902"/><line x1="328" x2="1296" y1="932" y2="932"/>
      <line x1="328" x2="1296" y1="962" y2="962"/>
    </g>

    <polygon fill="var(--days)" points="328,925 376,925 455,924 534,916 614,932 692,916 772,926 851,910 931,915 1010,915 1025,915 1085,993 328,993"/>

    <g class="invoice-bar"><rect x="361" y="647" width="14" height="346" fill="var(--contract)"/><rect x="361" y="606" width="14" height="41" fill="var(--extra)"/></g>
    <g class="invoice-bar"><rect x="378" y="628" width="14" height="365" fill="var(--paid)"/><rect x="378" y="606" width="14" height="22" fill="var(--unpaid)"/></g>
    <g class="invoice-bar"><rect x="441" y="647" width="14" height="346" fill="var(--contract)"/><rect x="441" y="616" width="14" height="31" fill="var(--plus)"/></g>
    <rect class="invoice-bar" x="458" y="616" width="14" height="377" fill="var(--paid)"/>
    <rect class="invoice-bar" x="521" y="612" width="14" height="381" fill="var(--contract)"/>
    <rect class="invoice-bar" x="538" y="612" width="14" height="381" fill="var(--paid)"/>
    <rect class="invoice-bar" x="601" y="705" width="14" height="288" fill="var(--contract)"/>
    <rect class="invoice-bar" x="618" y="705" width="14" height="288" fill="var(--unpaid)"/>
    <rect class="invoice-bar" x="676" y="805" width="14" height="188" fill="var(--contract)"/>
    <g class="invoice-bar"><rect x="693" y="831" width="14" height="162" fill="var(--paid)"/><rect x="693" y="806" width="14" height="25" fill="var(--unpaid)"/></g>
    <g class="invoice-bar"><rect x="756" y="852" width="14" height="141" fill="var(--contract)"/><rect x="756" y="831" width="14" height="21" fill="var(--extra)"/><rect x="756" y="715" width="14" height="116" fill="var(--plus)"/></g>
    <rect class="invoice-bar" x="773" y="714" width="14" height="279" fill="var(--paid)"/>
    <g class="invoice-bar"><rect x="836" y="742" width="14" height="251" fill="var(--contract)"/><rect x="836" y="465" width="14" height="277" fill="var(--plus)"/></g>
    <rect class="invoice-bar" x="853" y="464" width="14" height="529" fill="var(--paid)"/>
    <rect class="invoice-bar" x="916" y="625" width="14" height="368" fill="var(--contract)"/>
    <rect class="invoice-bar" x="933" y="624" width="14" height="369" fill="var(--unpaid)"/>
    <g class="invoice-bar"><rect x="994" y="841" width="14" height="152" fill="var(--contract)"/><rect x="994" y="816" width="14" height="25" fill="var(--extra)"/></g>
    <rect class="invoice-bar" x="1011" y="816" width="14" height="177" fill="var(--unpaid)"/>

    <g class="bar-note">
      <text transform="translate(357,646) rotate(-90)">€141.18</text>
      <text transform="translate(404,646) rotate(-90)">€-49.98</text>
      <text transform="translate(404,781) rotate(-90)">€1243.20</text>
      <text transform="translate(357,859) rotate(-90)">€1152.00</text>
    </g>

    <line x1="328.5" x2="328.5" y1="452" y2="993" stroke="#bbb"/>
    <line x1="328" x2="1296" y1="993.5" y2="993.5" stroke="#bbb"/>

    <g class="axis-label" text-anchor="end">
      <text x="316" y="487">€1700.00</text><text x="316" y="548">€1500.00</text>
      <text x="316" y="608">€1300.00</text><text x="316" y="668">€1100.00</text>
      <text x="316" y="728">€900.00</text><text x="316" y="789">€700.00</text>
      <text x="316" y="848">€500.00</text><text x="316" y="908">€300.00</text>
      <text x="316" y="968">€100.00</text>
    </g>
    <g class="axis-label">
      <text x="1302" y="816">30</text><text x="1302" y="846">25</text>
      <text x="1302" y="876">20</text><text x="1302" y="907">15</text>
      <text x="1302" y="937">10</text><text x="1302" y="965">05</text>
    </g>
    <g class="axis-label" text-anchor="middle">
      <text x="376" y="1024">JAN</text><text x="455" y="1024">FAB</text>
      <text x="534" y="1024">MAR</text><text x="614" y="1024">APR</text>
      <text x="692" y="1024">MAY</text><text x="772" y="1024">JUN</text>
      <text x="851" y="1024">JUL</text><text x="931" y="1024">AUG</text>
      <text x="1010" y="1024">SEP</text><text x="1089" y="1024">OCT</text>
      <text x="1168" y="1024">NOV</text><text x="1247" y="1024">DEC</text>
    </g>
    <text class="axis-title" transform="translate(237,988) rotate(-90)">AMOUNTS</text>
    <text class="axis-title" transform="translate(1363,942) rotate(90)">DAYS</text>
    <text class="axis-title" x="328" y="1059">MONTHS</text>

    <g class="invoice-tip">
      <rect class="tip-box" x="465" y="523" width="159" height="65" rx="3"/>
      <polygon class="tip-box" points="535,588 547,588 541,598"/>
      <text class="tip-id" x="473" y="541">TKZ19-035</text>
      <text class="tip-line" x="472" y="561">Paid : €1243.20</text>
      <text class="tip-line" x="472" y="580">Contract : €1243.20</text>
    </g>
    <g class="invoice-tip">
      <rect class="tip-box" x="855" y="524" width="159" height="84" rx="3"/>
      <polygon class="tip-box" points="925,608 937,608 931,618"/>
      <text class="tip-id" x="863" y="543">TKZ19-0547</text>
      <text class="tip-line" x="862" y="563">Unpaid : €1222.65</text>
      <text class="tip-line" x="862" y="582">Contract : €1222.65</text>
      <a href="#pay-TKZ19-0547"><text class="tip-pay" x="862" y="599">PAY NOW</text></a>
    </g>
  </svg>
</div>
</body>
</html>
```